Brickline Rentals podcast postcard

I've launched a podcast about apartment investing, ownership and management which is newly up on orbix and wavlino. I want to create a postcard that I can mail to my client base to get them to subscribe

```html
<!DOCTYPE html>
<html lang="en">
<head>
<meta charset="utf-8">
<title>Brickline Rentals Podcast Postcard</title>
<link rel="stylesheet" href="https://fonts.googleapis.com/css2?family=Roboto:ital,wght@0,300;0,400;0,500;0,700;0,900;1,900&display=swap">
<style>
  :root {
    --page-bg: #e6e7ea;
    --ink: #111111;
    --white: #f4f4f5;
    --light-grey: #e1e1e3;
    --purple: #362742;
    --purple-dark: #2e2139;
    --orange: #d88d2a;
    --band-brown: #634b2e;
    --sky: #5dc6dc;
  }
  html, body {
    margin: 0;
    width: 1200px;
    height: 1200px;
    overflow: hidden;
    background: var(--page-bg);
    font-family: "Roboto", Arial, sans-serif;
  }
  .postcard {
    position: absolute;
    left: 40px;
    top: 226px;
    width: 1250px;
    height: 835px;
    transform: scale(0.896);
    transform-origin: top left;
    overflow: hidden;
    background: var(--white);
    box-shadow: 0 8px 24px rgba(0,0,0,0.25);
  }
  .postcard__shapes {
    position: absolute;
    inset: 0;
  }
  .brand {
    position: absolute;
    left: 52px;
    top: 58px;
    margin: 0;
    line-height: 1;
  }
  .brand__top {
    display: block;
    font-size: 50px;
    font-weight: 700;
    letter-spacing: 3px;
    color: var(--ink);
  }
  .brand__bottom {
    display: block;
    margin-top: 12px;
    font-size: 64px;
    font-weight: 700;
    color: var(--orange);
  }
  .services {
    position: absolute;
    left: 0;
    top: 205px;
    margin: 0;
    padding: 0;
    list-style: none;
  }
  .service {
    position: relative;
    height: 115px;
    display: flex;
    align-items: center;
  }
  .service:first-child { height: 130px; }
  .service__icon {
    position: absolute;
    left: 80px;
    width: 80px;
    height: 80px;
  }
  .service__label {
    position: absolute;
    left: 190px;
    font-size: 56px;
    font-weight: 500;
    color: var(--sky);
    white-space: nowrap;
  }
  .intro {
    position: absolute;
    left: 52px;
    top: 628px;
    width: 470px;
    margin: 0;
    font-size: 21.5px;
    font-weight: 500;
    line-height: 1.3;
    color: var(--ink);
  }
  .contact {
    position: absolute;
    right: 42px;
    top: 620px;
    text-align: right;
    color: var(--ink);
  }
  .contact__lead {
    margin: 0;
    font-size: 21.5px;
    font-weight: 500;
  }
  .contact__phone {
    margin: 0;
    font-size: 82px;
    font-weight: 900;
    font-style: italic;
    line-height: 1;
    letter-spacing: 1px;
  }
  .subscribe {
    position: absolute;
    left: 52px;
    right: 42px;
    top: 758px;
    margin: 0;
    font-size: 56px;
    line-height: 1;
    white-space: nowrap;
    display: flex;
    justify-content: space-between;
  }
  .subscribe__call {
    font-weight: 700;
    color: #ffffff;
  }
  .subscribe__where {
    font-weight: 400;
    color: var(--sky);
  }
</style>
</head>
<body>
  <article class="postcard">
    <svg class="postcard__shapes" width="1250" height="835" viewBox="0 0 1250 835">
      <defs>
        <linearGradient id="keyPhotoTone" x1="0" y1="0" x2="1" y2="0">
          <stop offset="0" stop-color="#07090b"/>
          <stop offset="0.55" stop-color="#0d1417"/>
          <stop offset="0.75" stop-color="#1d3a42"/>
          <stop offset="0.88" stop-color="#2b4a50"/>
          <stop offset="0.9" stop-color="#4a1a10"/>
          <stop offset="1" stop-color="#5a2414"/>
        </linearGradient>
      </defs>
      <rect class="key-photo" x="460" y="0" width="790" height="605" fill="url(#keyPhotoTone)" role="img" aria-label="Photo of a key with a house-shaped keyring in a door lock"/>
      <rect class="accent-band" x="525" y="105" width="725" height="100" fill="var(--band-brown)" opacity="0.92"/>
      <polygon class="title-panel" points="0,0 460,0 585,205 0,205" fill="var(--white)"/>
      <polygon class="service-panel" points="0,205 585,205 845,605 0,605" fill="var(--purple)"/>
      <polygon class="service-row-shade" points="0,335 670,335 676,345 0,345" fill="var(--purple-dark)"/>
      <polygon class="service-row-shade" points="0,450 745,450 751,460 0,460" fill="var(--purple-dark)"/>
      <rect class="info-strip" x="0" y="605" width="1250" height="133" fill="var(--light-grey)"/>
      <polygon class="phone-panel" points="523,605 1250,605 1250,738 650,738" fill="var(--orange)"/>
      <rect class="subscribe-bar" x="0" y="738" width="1250" height="97" fill="var(--purple)"/>
    </svg>

    <h1 class="brand">
      <span class="brand__top">BRICKLINE</span>
      <span class="brand__bottom">RENTALS</span>
    </h1>

    <ul class="services">
      <li class="service">
        <svg class="service__icon" viewBox="0 0 80 80" aria-hidden="true">
          <circle cx="44" cy="18" r="15" fill="var(--orange)"/>
          <text x="44" y="25" text-anchor="middle" font-family="Roboto, sans-serif" font-weight="700" font-size="20" fill="var(--purple)">$</text>
          <path d="M14 58 L30 46 Q36 42 44 44 L56 47 Q60 49 57 53 L44 53 L62 50 Q70 46 74 50 L52 64 Q46 67 38 65 L24 64 Z" fill="var(--orange)"/>
          <path d="M6 62 L16 72 L12 76 L2 66 Z" fill="var(--orange)"/>
        </svg>
        <span class="service__label">INVESTING</span>
      </li>
      <li class="service">
        <svg class="service__icon" viewBox="0 0 80 80" aria-hidden="true">
          <path d="M40 6 L76 36 L70 42 L64 37 L64 72 L16 72 L16 37 L10 42 L4 36 Z" fill="var(--orange)"/>
          <rect x="56" y="10" width="8" height="16" fill="var(--orange)"/>
          <circle cx="40" cy="42" r="8" fill="var(--purple)"/>
          <path d="M26 66 Q26 52 40 52 Q54 52 54 66 Z" fill="var(--purple)"/>
        </svg>
        <span class="service__label">OWNERSHIP</span>
      </li>
      <li class="service">
        <svg class="service__icon" viewBox="0 0 80 80" aria-hidden="true">
          <path d="M26 16 L26 10 L50 10 L50 16 L56 16 L56 22 L44 22 L44 14 L32 14 L32 22 Z" fill="var(--orange)"/>
          <rect x="2" y="20" width="64" height="44" rx="5" fill="var(--orange)"/>
          <rect x="2" y="38" width="64" height="3" fill="var(--purple)"/>
          <rect x="30" y="34" width="8" height="10" fill="var(--purple)"/>
          <circle cx="64" cy="60" r="16" fill="var(--purple)"/>
          <circle cx="64" cy="60" r="13" fill="var(--orange)"/>
          <text x="64" y="67" text-anchor="middle" font-family="Roboto, sans-serif" font-weight="700" font-size="19" fill="var(--purple)">$</text>
        </svg>
        <span class="service__label">MANAGEMENT</span>
      </li>
    </ul>

    <p class="intro">Our new podcast covers apartment investing, ownership and management. Listen now and subscribe on orbix and wavlino!</p>

    <div class="contact">
      <p class="contact__lead">FOR ANY ADDITIONAL QUESTIONS PLEASE CALL OR TEXT</p>
      <p class="contact__phone">123 456 7890</p>
    </div>

    <p class="subscribe">
      <span class="subscribe__call">SUBSCRIBE NOW :</span>
      <span class="subscribe__where">ON ORBIX &amp; WAVLINO</span>
    </p>
  </article>
</body>
</html>
```